Simple Business Cards for Self-employed Coach

Simple business card with a design that includes the QLT logo.
Using either only the logo color or additional colors that match the logo.

Meridian Guides reach deeply into the past, gathering wisdom from East and West, while still staying current with the frontiers of new discovery in cognitive science, genetics, and other disciplines. see https://www.brightharborpath.example/what-is-integral-coaching/

Target Market(s)

Coaching Clients in Tokyo /Asia; in business organizations, but also outside

Industry/Entity Type

Life Coaching

Contact Information for Business Card

Lukas Brenning
Certified Meridian Guide

3-2-48 Kamiyoshi
Nakarino 164-0392
Tokyo, Japan

Phone: +81 70 4817 5062
E-Mail: lukas.brenning@mailora.example

Font styles to use
Sans Serif

Colors
00a990

Requirements
Must have
• include uploaded logo
• color fitting with QLT logo color
Nice to have
• simple, elegant design
Should not have
• clutter

```html
<!DOCTYPE html>
<html lang="en">
<head>
<meta charset="utf-8">
<title>Lukas Brenning – Business Card</title>
<link rel="stylesheet" href="https://fonts.googleapis.com/css2?family=Roboto:wght@300;400;500&display=swap">
<style>
  :root {
    --backdrop: #1b1819;
    --brand-teal: #1f7f78;
    --leaf-green: #0aa553;
    --spring-green: #5cc070;
    --pale-lime: #dfe9a6;
    --cream: #fbf8df;
    --paper: #ffffff;
    --ink: #1a1a1a;
  }
  html, body {
    margin: 0;
    width: 1200px;
    height: 1200px;
    overflow: hidden;
    background: var(--backdrop);
    font-family: "Roboto", Arial, sans-serif;
  }
  .business-card {
    position: absolute;
    left: 160px;
    top: 351px;
    width: 880px;
    height: 500px;
    overflow: hidden;
    background: var(--paper);
  }
  .card-artwork {
    position: absolute;
    inset: 0;
    background:
      radial-gradient(ellipse 70% 40% at 20% 20%, rgba(160, 170, 90, 0.35), transparent 70%),
      linear-gradient(180deg,
        var(--leaf-green) 0%,
        var(--spring-green) 16%,
        #a9d98a 34%,
        var(--pale-lime) 50%,
        var(--cream) 72%,
        var(--paper) 100%);
  }
  .logo-tab {
    position: absolute;
    left: 0;
    top: 181px;
    width: 440px;
    height: 136px;
    background: var(--paper);
    border-radius: 0 68px 68px 0;
    display: flex;
    align-items: center;
    justify-content: center;
    gap: 16px;
    padding-right: 30px;
    box-sizing: border-box;
  }
  .logo-square {
    width: 34px;
    height: 34px;
    background: var(--brand-teal);
  }
  .brand-name {
    font-family: "Roboto", Arial, sans-serif;
    font-weight: 500;
    font-size: 54px;
    letter-spacing: 8px;
    color: var(--brand-teal);
    line-height: 1;
  }
  .contact-block {
    position: absolute;
    left: 441px;
    top: 92px;
    color: var(--ink);
  }
  .person-name {
    margin: 0;
    font-weight: 400;
    font-size: 35px;
    line-height: 42px;
    color: var(--paper);
  }
  .person-title {
    margin: 0;
    font-weight: 300;
    font-size: 25px;
    line-height: 32px;
  }
  .address, .reach {
    margin: 0;
    font-weight: 300;
    font-size: 30px;
    line-height: 37px;
    font-style: normal;
  }
  .address { margin-top: 38px; }
  .reach { margin-top: 40px; }
</style>
</head>
<body>
  <section class="business-card">
    <div class="card-artwork" role="img" aria-label="Painted green brush strokes fading into pale yellow"></div>

    <div class="logo-tab">
      <span class="logo-square"></span>
      <span class="brand-name">QLT</span>
    </div>

    <div class="contact-block">
      <h1 class="person-name">Lukas Brenning</h1>
      <p class="person-title">Certified Meridian Guide</p>
      <address class="address">
        3-2-48 Kamiyoshi<br>
        Nakarino 164-0392<br>
        Tokyo, Japan
      </address>
      <p class="reach">
        +81 70 4817 5062<br>
        lukas.brenning@mailora.example
      </p>
    </div>
  </section>
</body>
</html>
```